Our swimming pool service needs your help with letterhead

Letterhead for small swimming pool service- We would like a professional look with a creative layout- must be compatible with LedgerNest forms (sample attached)
No more than 2 colors in graphics

Target Market(s)

Homeowners/ Contractors

Font styles to use
Sans Serif

Colors
33a6d7
85cae6

Requirements
Must have
• Logo (file attached)
• Compatible with LedgerNest (sample attached)
• Mailing address- P.O. Box 58, Cedar Hollow NY 11592
• phone- (631) 529-6180
• email- marcdoylewater@mailbrook.net
• Licensed & Insured
Nice to have
• Small slogan- Examples:Family owned and operated for 25 years, 25 years of trusted service
• Creative layout
Should not have
• Blue color must be same as blue in our logo
• No thick lines of color
• No design in middle of page

```html
<!DOCTYPE html>
<html lang="en">
<head>
<meta charset="utf-8">
<title>Marc D. Doyle Pool Service – Letterhead</title>
<link rel="stylesheet" href="https://fonts.googleapis.com/css2?family=Open+Sans:wght@400;600&family=Raleway:wght@200&display=swap">
<style>
  :root {
    --backdrop: #d8dcdd;
    --paper: #ffffff;
    --navy: #2a4878;
    --navy-deep: #1f3a66;
    --pool-blue: #33a6d7;
    --pool-blue-light: #85cae6;
    --ink-grey: #6d7175;
    --rule-grey: #c9cdd0;
    --slogan-grey: #cdd1d4;
  }
  * { box-sizing: border-box; margin: 0; padding: 0; }
  html, body {
    width: 1200px;
    height: 784px;
    overflow: hidden;
    background: var(--backdrop);
  }
  .letterhead {
    position: absolute;
    left: 306px;
    top: 12px;
    width: 588px;
    height: 760px;
    background: var(--paper);
    box-shadow: 0 2px 10px rgba(0, 0, 0, 0.12);
    overflow: hidden;
  }
  .corner-tab {
    position: absolute;
    left: 10px;
    top: 12px;
    width: 40px;
    height: 13px;
    background: linear-gradient(90deg, var(--pool-blue), #4f8fd1);
  }
  .margin-rule {
    position: absolute;
    left: 16px;
    top: 70px;
    bottom: 0;
    width: 7px;
    background: linear-gradient(90deg, var(--navy-deep), var(--navy));
  }
  .brand {
    position: absolute;
    left: 44px;
    top: 72px;
    display: flex;
    align-items: center;
    gap: 8px;
  }
  .brand-dot {
    width: 18px;
    height: 18px;
    border-radius: 50%;
    background: var(--pool-blue);
    flex: none;
  }
  .brand-name {
    font-family: "Open Sans", sans-serif;
    font-weight: 600;
    font-size: 17px;
    line-height: 1.15;
    letter-spacing: 0.06em;
    text-transform: uppercase;
    color: var(--navy);
  }
  .contact {
    position: absolute;
    left: 410px;
    top: 104px;
    width: 164px;
    padding-left: 12px;
    border-left: 1px solid var(--rule-grey);
    font-family: "Open Sans", sans-serif;
    font-size: 8.5px;
    line-height: 1.45;
    color: var(--ink-grey);
    list-style: none;
  }
  .contact-item {
    display: flex;
    align-items: flex-start;
    gap: 5px;
    margin-bottom: 2px;
    white-space: nowrap;
  }
  .contact-icon {
    width: 9px;
    height: 9px;
    flex: none;
    margin-top: 2px;
  }
  .licence {
    margin-top: 4px;
    font-weight: 600;
    color: var(--navy);
  }
  .slogan {
    position: absolute;
    left: 96px;
    bottom: 70px;
    font-family: "Raleway", sans-serif;
    font-weight: 200;
    font-size: 23px;
    font-variant-numeric: lining-nums;
    letter-spacing: 0.04em;
    text-transform: uppercase;
    color: var(--slogan-grey);
  }
</style>
</head>
<body>
  <main class="letterhead">
    <div class="corner-tab"></div>
    <div class="margin-rule"></div>

    <header class="brand">
      <span class="brand-dot"></span>
      <h1 class="brand-name">Marc D. Doyle<br>Pool Service</h1>
    </header>

    <ul class="contact">
      <li class="contact-item">
        <svg class="contact-icon" viewBox="0 0 10 10" aria-hidden="true">
          <circle cx="5" cy="5" r="5" fill="#33a6d7"/>
          <path d="M5 2.2a1.8 1.8 0 0 0-1.8 1.8C3.2 5.4 5 7.8 5 7.8S6.8 5.4 6.8 4A1.8 1.8 0 0 0 5 2.2z" fill="#fff"/>
        </svg>
        <span>P.O. Box 58, Cedar Hollow<br>NY 11592</span>
      </li>
      <li class="contact-item">
        <svg class="contact-icon" viewBox="0 0 10 10" aria-hidden="true">
          <circle cx="5" cy="5" r="5" fill="#33a6d7"/>
          <path d="M3.3 2.5l1 1.2-.5.7c.4.8 1 1.4 1.8 1.8l.7-.5 1.2 1-.6.9C5 7.4 2.6 5 2.4 3.1z" fill="#fff"/>
        </svg>
        <span>(631) 529-6180</span>
      </li>
      <li class="contact-item">
        <svg class="contact-icon" viewBox="0 0 10 10" aria-hidden="true">
          <circle cx="5" cy="5" r="5" fill="#33a6d7"/>
          <rect x="2.5" y="3.3" width="5" height="3.4" fill="#fff"/>
          <path d="M2.5 3.3L5 5.2 7.5 3.3" stroke="#33a6d7" stroke-width="0.6" fill="none"/>
        </svg>
        <span>marcdoylewater@mailbrook.net</span>
      </li>
      <li class="contact-item licence">
        <svg class="contact-icon" viewBox="0 0 10 10" aria-hidden="true">
          <circle cx="5" cy="5" r="5" fill="#33a6d7"/>
          <path d="M2.8 5.1l1.5 1.5 2.9-3" stroke="#fff" stroke-width="1.1" fill="none"/>
        </svg>
        <span>Licensed &amp; Insured</span>
      </li>
    </ul>

    <p class="slogan">25 Years of Trusted Service</p>
  </main>
</body>
</html>
```